Minimalistic and chic product labels required for tea packaging

We need a Label Sticker Design for our tea company that is minimalistic, simple and chic.

We have 2 categories of tea: artisan tea (single flavoured tea e.g. green and black) and herbal teas (e.g. mixuture of herbs and flowers). We would like to have the designs to tell the difference of artisan tea and herbal tea, this can be done by having different colours to tell the difference or if there are other design features used.

We would also like to have colourful colours on our herbal tea range, preferably either a light and chic pastel colour palette or bright and chic colour palette.

The labels will be stuck onto a white pouch. The final design should also include the variety of colour palettes that can be used in AI format with the label. Preferred label measurements in 9cm width, and 11cm height. Our logo is attached.

Beauty and wellness

Health And Wellness

Requirements
Must have
• 2 x labels (front and back)
Front label must include logo, text to include tea type and weight
Back label must include text space to write description
Nice to have
• Simple and chic label design to stick onto a white pouch
Should not have
• Must not have too much graphic and pictures

```html
<!DOCTYPE html>
<html lang="en">
<head>
<meta charset="utf-8">
<title>Verdalia Tea Labels</title>
<link rel="stylesheet" href="https://fonts.googleapis.com/css2?family=Jost:wght@300;400&family=Marcellus&display=swap">
<style>
  :root {
    --canvas: #ffffff;
    --heading: #4a4a4a;
    --artisan-ink: #f39c27;
    --artisan-paper: #fde9c1;
    --artisan-text: #d9861c;
    --herbal-ink: #2e5a27;
    --herbal-paper: #c3d596;
    --herbal-text: #2e5a27;
    --herbal-light: #dbe7ae;
  }
  * { box-sizing: border-box; margin: 0; padding: 0; }
  html, body { width: 1200px; height: 900px; overflow: hidden; background: var(--canvas); }
  .sheet { position: relative; width: 1200px; height: 900px; font-family: "Jost", sans-serif; }

  .column-title {
    position: absolute; top: 76px; width: 200px; text-align: center;
    font-family: "Jost", sans-serif; font-weight: 300; font-size: 40px;
    letter-spacing: 1px; color: var(--heading);
  }
  .column-title--front { left: 353px; }
  .column-title--back { left: 644px; }

  .label {
    position: absolute; width: 255px; height: 311px;
    background: var(--paper); color: var(--ink);
  }
  .label--artisan { --ink: var(--artisan-ink); --paper: var(--artisan-paper); --soft: var(--artisan-text); --band-text: var(--artisan-paper); }
  .label--herbal  { --ink: var(--herbal-ink);  --paper: var(--herbal-paper);  --soft: var(--herbal-text);  --band-text: var(--herbal-light); }
  .label--front { left: 327px; }
  .label--back  { left: 618px; }
  .row-artisan { top: 164px; }
  .row-herbal  { top: 531px; }

  .label__frame { position: absolute; inset: 0; width: 255px; height: 311px; }
  .frame-line { fill: none; stroke: var(--ink); stroke-width: 2.2; }
  .frame-fill { fill: var(--ink); }
  .frame-dot { fill: var(--ink); }
  .arc-text {
    fill: var(--ink); font-family: "Jost", sans-serif; font-weight: 400;
    font-size: 11.5px; letter-spacing: 1.2px;
  }

  .brand {
    position: absolute; left: 0; width: 255px;
    display: flex; flex-direction: column; align-items: center; gap: 8px;
  }
  .brand__mark {
    width: 26px; height: 26px; border-radius: 50%;
    border: 1.6px solid var(--ink);
  }
  .brand__name {
    font-family: "Jost", sans-serif; font-weight: 300; font-size: 26px;
    letter-spacing: 1px; color: var(--ink); line-height: 1;
  }
  .label--front .brand { top: 94px; }
  .label--back .brand { top: 38px; }

  .tea-type {
    position: absolute; left: 10px; top: 218px; width: 235px; height: 41px;
    display: flex; align-items: center; justify-content: center;
    font-family: "Marcellus", serif; font-size: 20px; letter-spacing: 0.5px;
    color: var(--band-text);
  }
  .net-weight {
    position: absolute; left: 10px; top: 266px; width: 235px; text-align: center;
    font-family: "Jost", sans-serif; font-weight: 300; font-size: 14px; color: var(--soft);
  }
  .herbal-net { color: var(--herbal-ink); }

  .description {
    position: absolute; left: 12px; top: 137px; width: 231px; text-align: center;
    font-family: "Jost", sans-serif; font-weight: 300; font-size: 13px; line-height: 17.6px;
    color: var(--band-text);
  }
  .label--herbal .description { color: var(--herbal-light); }
</style>
</head>
<body>
<main class="sheet">
  <h2 class="column-title column-title--front">FRONT</h2>
  <h2 class="column-title column-title--back">BACK</h2>

  <!-- Artisan front -->
  <section class="label label--artisan label--front row-artisan">
    <svg class="label__frame" viewBox="0 0 255 311" aria-hidden="true">
      <defs><path id="arc-artisan" d="M58,40 C90,16 165,16 197,40"/></defs>
      <path class="frame-line" d="M10,304 V48 H41 C62,30 193,30 214,48 H245 V304 Z"/>
      <circle class="frame-dot" cx="56" cy="46" r="2"/>
      <circle class="frame-dot" cx="199" cy="46" r="2"/>
      <text class="arc-text"><textPath href="#arc-artisan" startOffset="50%" text-anchor="middle">PREMIUM QUALITY</textPath></text>
      <rect class="frame-fill" x="10" y="218" width="235" height="41"/>
      <line class="frame-line" x1="10" y1="261" x2="245" y2="261"/>
    </svg>
    <div class="brand"><span class="brand__mark"></span><span class="brand__name">Verdalia</span></div>
    <div class="tea-type">ARTISAN TEA</div>
    <div class="net-weight">Net wt. 10g</div>
  </section>

  <!-- Artisan back -->
  <section class="label label--artisan label--back row-artisan">
    <svg class="label__frame" viewBox="0 0 255 311" aria-hidden="true">
      <path class="frame-line" d="M9,304 V48 H28 Q38,48 40,40 C60,0 195,0 215,40 Q217,48 227,48 H246 V304 Z"/>
      <rect class="frame-fill" x="9" y="128" width="237" height="176"/>
    </svg>
    <div class="brand"><span class="brand__mark"></span><span class="brand__name">Verdalia</span></div>
    <p class="description">Lorem ipsum dolor sit amet, consectetuer adipiscing elit, sed diam nonummy nibh euismod tincidunt ut laoreet dolore magna aliquam erat volutpat. Ut wisi enim ad minim veniam, quis nostrud exerci tation ullamcorper suscipit lobortis nisl ut aliquip ex ea commo</p>
  </section>

  <!-- Herbal front -->
  <section class="label label--herbal label--front row-herbal">
    <svg class="label__frame" viewBox="0 0 255 311" aria-hidden="true">
      <defs><path id="arc-herbal" d="M58,40 C90,16 165,16 197,40"/></defs>
      <path class="frame-line" d="M10,304 V48 H41 C62,30 193,30 214,48 H245 V304 Z"/>
      <circle class="frame-dot" cx="56" cy="46" r="2"/>
      <circle class="frame-dot" cx="199" cy="46" r="2"/>
      <text class="arc-text"><textPath href="#arc-herbal" startOffset="50%" text-anchor="middle">PREMIUM QUALITY</textPath></text>
      <rect class="frame-fill" x="10" y="218" width="235" height="41"/>
      <line class="frame-line" x1="10" y1="261" x2="245" y2="261"/>
    </svg>
    <div class="brand"><span class="brand__mark"></span><span class="brand__name">Verdalia</span></div>
    <div class="tea-type">HERBAL TEA</div>
    <div class="net-weight herbal-net">Net wt. 10g</div>
  </section>

  <!-- Herbal back -->
  <section class="label label--herbal label--back row-herbal">
    <svg class="label__frame" viewBox="0 0 255 311" aria-hidden="true">
      <path class="frame-line" d="M9,304 V48 H28 Q38,48 40,40 C60,0 195,0 215,40 Q217,48 227,48 H246 V304 Z"/>
      <rect class="frame-fill" x="9" y="128" width="237" height="176"/>
    </svg>
    <div class="brand"><span class="brand__mark"></span><span class="brand__name">Verdalia</span></div>
    <p class="description">Lorem ipsum dolor sit amet, consectetuer adipiscing elit, sed diam nonummy nibh euismod tincidunt ut laoreet dolore magna aliquam erat volutpat. Ut wisi enim ad minim veniam, quis nostrud exerci tation ullamcorper suscipit lobortis nisl ut aliquip ex ea commo</p>
  </section>
</main>
</body>
</html>
```